Business Card Design

Needing a business card design similar to the business card that is attached.

Industry/Entity Type

Business

Contact Information for Business Card

Design similar to the b-cards that is attached.

```html
<!DOCTYPE html>
<html lang="en">
<head>
<meta charset="utf-8">
<title>Business Cards</title>
<link rel="stylesheet" href="https://fonts.googleapis.com/css2?family=Open+Sans:wght@400;600;700&family=Roboto+Condensed:wght@400;700&display=swap">
<style>
  :root {
    --bg: #e9e6e1;
    --card: #ffffff;
    --ink: #2b2b2b;
    --green: #6fae1e;
    --red: #d8342c;
    --blue: #5b8fd6;
    --sky: #2fa3d6;
  }
  html, body {
    margin: 0;
    width: 1200px;
    height: 1023px;
    overflow: hidden;
    background: var(--bg);
    font-family: "Open Sans", Arial, sans-serif;
  }
  p { margin: 0; }
  .canvas { position: relative; width: 1200px; height: 1023px; }
  .card {
    position: absolute;
    width: 540px;
    height: 309px;
    background: var(--card);
    box-shadow: 0 6px 18px rgba(0,0,0,0.18);
    box-sizing: border-box;
    white-space: nowrap;
  }
  .card--thermal { left: 80px; top: 150px; }
  .card--realty { left: 580px; top: 560px; }

  .brand { position: absolute; display: flex; align-items: center; gap: 10px; }
  .brand__mark { width: 44px; height: 44px; flex: none; }
  .brand__name { font-weight: 700; margin: 0; line-height: 1; }

  .card--thermal .brand { left: 26px; top: 22px; }
  .card--thermal .brand__name { color: var(--green); font-size: 30px; letter-spacing: -0.5px; }
  .card--thermal .brand__mark { border-radius: 50%; background: var(--green); }
  .tagline {
    position: absolute; left: 82px; top: 66px;
    color: var(--red); font-weight: 700; font-size: 13px; letter-spacing: 1px;
  }

  .person { position: absolute; }
  .person__name { color: var(--ink); font-weight: 700; font-size: 19px; line-height: 1.3; }
  .person__title { color: var(--blue); font-size: 15px; line-height: 1.3; margin-top: 2px; }
  .person__phone { color: var(--red); font-weight: 600; font-size: 19px; line-height: 1.3; margin-top: 4px; }
  .card--thermal .person { left: 120px; top: 100px; }
  .card--thermal .person__phone { margin-left: 70px; }

  .promo { position: absolute; right: 24px; top: 166px; font-size: 13px; line-height: 1.4; color: var(--ink); }
  .promo .link { color: var(--red); }

  .address { position: absolute; left: 26px; bottom: 22px; font-size: 13px; line-height: 1.45; color: var(--ink); font-style: normal; }
  .address .link { color: var(--red); }

  .card--realty .brand { left: 26px; top: 30px; }
  .card--realty .brand__mark { border-radius: 8px; background: var(--sky); }
  .card--realty .brand__name { color: var(--red); font-family: "Roboto Condensed", "Arial Narrow", sans-serif; font-size: 34px; }
  .card--realty .person { left: 120px; top: 104px; font-family: "Roboto Condensed", "Arial Narrow", sans-serif; }
  .card--realty .person__name { font-size: 23px; }
  .card--realty .person__title { font-size: 18px; }
  .card--realty .person__phone { font-size: 22px; font-weight: 400; }
  .lines { position: absolute; right: 24px; top: 120px; font-size: 15px; line-height: 1.45; color: var(--ink); }
  .lines .label { color: var(--red); }
  .lines .link { color: var(--blue); font-weight: 600; }
  .card--realty .address .link { font-weight: 600; }
</style>
</head>
<body>
<main class="canvas">
  <section class="card card--thermal">
    <div class="brand">
      <span class="brand__mark"></span>
      <h1 class="brand__name">NorthPeak Thermal, Inc.</h1>
    </div>
    <p class="tagline">Heat without a flame!</p>
    <div class="person">
      <p class="person__name">Daniel Okonkwo</p>
      <p class="person__title">M. E. &amp; Certified Geothermal Designer</p>
      <p class="person__phone">(206) 555-0147</p>
    </div>
    <div class="promo">
      To learn about Geo<br>Visit our Website<br><span class="link">NorthPeakThermal.com</span>
    </div>
    <address class="address">
      4210 S 88th PL# B200<br>Auburn, WA 98001<br><span class="link">Dan@NorthPeakThermal.com</span>
    </address>
  </section>

  <section class="card card--realty">
    <div class="brand">
      <span class="brand__mark"></span>
      <h1 class="brand__name">Harbor Key Realty, Inc.</h1>
    </div>
    <div class="person">
      <p class="person__name">Daniel Okonkwo</p>
      <p class="person__title">Managing Broker</p>
      <p class="person__phone">(206) 555-0147</p>
    </div>
    <div class="lines">
      <span class="label">Phone:</span> 253-555-0182<br>
      <span class="label">Fax:</span> (253) 555-0193<br>
      <span class="link">Dan@HarborKeyRealty.com</span>
    </div>
    <address class="address">
      4210 S 88th PL# B200<br>Auburn, WA 98001<br><span class="link">HarborKeyRealty.com</span>
    </address>
  </section>
</main>
</body>
</html>
```